Veltor & Aero Services Business Card Design

a specialised consulting company, aviation specialist, like to have use blue colour on white background.
back of card to have printed-
NDT Expertise:
INSPECTION & TESTING CONSULTING
TRAINING & EDUCATION
CERTIFICATION SERVICES
LEVEL 3 SERVICES
TORVEX / AUDITING
INSPECTION SYSTEMS

Target Market(s)

Mainly the aerospace industry, manufacturers and airframe/engine overhaul companies.

Industry/Entity Type

Business

Contact Information for Business Card

Veltor & Aero Services

Trevor Mulcahy JP

+61 (0)437610582
veltoraeroservices@pindramail.com

Font styles to use
Serif

Colors
3276b4
32a5d5

Requirements
Must have
• aviation style logo with letters VAS part of or adjacent to.

then company name: Veltor & Aero Services

then name in slightly smaller font : Trevor Mulcahy JP

then phone and email details

Back of card, as per brief, but all text to be centred

```html
<!DOCTYPE html>
<html lang="en">
<head>
<meta charset="utf-8">
<title>Veltor &amp; Aero Services – Business Card</title>
<link rel="stylesheet" href="https://fonts.googleapis.com/css2?family=Merriweather:ital,wght@0,400;0,700;0,900;1,400;1,700&display=swap">
<style>
  :root {
    --page: #eceef1;
    --grey-card: #dcdee2;
    --grey-light: #e7e8eb;
    --grey-edge: #c9cbd0;
    --blue: #3a55a4;
    --blue-deep: #2b418a;
    --blue-edge: #213576;
    --ink-blue: #2d4898;
    --text-light: #eef1f8;
  }
  * { box-sizing: border-box; margin: 0; padding: 0; }
  html, body { width: 1200px; height: 720px; overflow: hidden; }
  body {
    background: var(--page);
    font-family: "Merriweather", Georgia, serif;
    display: flex;
    align-items: center;
    justify-content: center;
    gap: 60px;
  }
  .card {
    position: relative;
    width: 520px;
    height: 297px;
    overflow: hidden;
    box-shadow: 0 6px 18px rgba(30, 40, 70, 0.18);
  }
  .card-shapes { position: absolute; inset: 0; width: 100%; height: 100%; }

  /* front */
  .identity {
    position: absolute;
    top: 18px;
    right: 30px;
    display: flex;
    flex-direction: column;
    align-items: flex-end;
    text-align: right;
  }
  .brand-mark {
    display: flex;
    align-items: center;
    gap: 8px;
    margin-bottom: 6px;
  }
  .brand-dot {
    width: 22px;
    height: 22px;
    border-radius: 50%;
    background: var(--ink-blue);
  }
  .brand-name {
    font-weight: 900;
    font-size: 22px;
    letter-spacing: 2px;
    color: var(--ink-blue);
    line-height: 1;
  }
  .company-name {
    font-weight: 900;
    font-size: 22px;
    color: var(--ink-blue);
    line-height: 1.2;
  }
  .person-name {
    font-style: italic;
    font-weight: 700;
    font-size: 16px;
    color: var(--ink-blue);
    margin-top: 3px;
    line-height: 1.2;
  }
  .contact-list {
    position: absolute;
    left: 30px;
    bottom: 30px;
    list-style: none;
  }
  .contact-item {
    display: flex;
    align-items: center;
    gap: 12px;
    color: var(--text-light);
    font-size: 13.5px;
    margin-top: 10px;
  }
  .contact-icon {
    width: 24px;
    height: 24px;
    background: var(--text-light);
    border-radius: 5px;
    display: flex;
    align-items: center;
    justify-content: center;
    flex: none;
  }

  /* back */
  .expertise {
    position: absolute;
    left: 0;
    right: 0;
    top: 104px;
    text-align: center;
    color: var(--text-light);
  }
  .expertise-title {
    font-weight: 900;
    font-size: 24px;
    line-height: 1.1;
    margin-bottom: 8px;
  }
  .expertise-list { list-style: none; }
  .expertise-list li {
    font-weight: 700;
    font-size: 11.5px;
    letter-spacing: 0.4px;
    line-height: 1.55;
  }
</style>
</head>
<body>

  <section class="card card-front" aria-label="Business card front">
    <svg class="card-shapes" viewBox="0 0 520 297" aria-hidden="true">
      <rect width="520" height="297" fill="var(--grey-card)"/>
      <polygon points="0,0 300,0 90,165 0,165" fill="var(--grey-light)"/>
      <polygon points="0,152 300,152 322,118 520,118 520,297 0,297" fill="var(--blue-edge)"/>
      <polygon points="0,162 304,162 326,128 520,128 520,297 0,297" fill="var(--blue)"/>
      <polygon points="0,230 80,162 300,162 110,297 0,297" fill="var(--blue-deep)" opacity="0.75"/>
    </svg>
    <div class="identity">
      <div class="brand-mark">
        <span class="brand-dot" aria-hidden="true"></span>
        <span class="brand-name">VAS</span>
      </div>
      <h1 class="company-name">Veltor &amp; Aero Services</h1>
      <p class="person-name">Trevor Mulcahy JP</p>
    </div>
    <ul class="contact-list">
      <li class="contact-item">
        <span class="contact-icon">
          <svg width="14" height="14" viewBox="0 0 24 24" aria-hidden="true"><path fill="var(--blue)" d="M6.6 10.8a15.1 15.1 0 0 0 6.6 6.6l2.2-2.2a1 1 0 0 1 1-.25 11.4 11.4 0 0 0 3.6.57 1 1 0 0 1 1 1V20a1 1 0 0 1-1 1A17 17 0 0 1 3 4a1 1 0 0 1 1-1h3.5a1 1 0 0 1 1 1c0 1.25.2 2.45.57 3.57a1 1 0 0 1-.25 1z"/></svg>
        </span>
        <span class="contact-text">+61 (0)437610582</span>
      </li>
      <li class="contact-item">
        <span class="contact-icon">
          <svg width="15" height="12" viewBox="0 0 24 18" aria-hidden="true"><rect x="1" y="1" width="22" height="16" rx="2" fill="var(--blue)"/><path d="M2 2l10 8 10-8" fill="none" stroke="var(--text-light)" stroke-width="2"/></svg>
        </span>
        <span class="contact-text">veltoraeroservices@pindramail.com</span>
      </li>
    </ul>
  </section>

  <section class="card card-back" aria-label="Business card back">
    <svg class="card-shapes" viewBox="0 0 520 297" aria-hidden="true">
      <rect width="520" height="297" fill="var(--grey-card)"/>
      <polygon points="0,52 232,52 254,78 276,52 520,52 520,297 0,297" fill="var(--grey-edge)"/>
      <polygon points="0,60 228,60 254,90 280,60 520,60 520,297 0,297" fill="var(--blue)"/>
      <polygon points="520,210 520,297 300,297 470,60 520,60" fill="var(--blue-deep)" opacity="0.55"/>
    </svg>
    <div class="expertise">
      <h2 class="expertise-title">NDT Expertise:</h2>
      <ul class="expertise-list">
        <li>INSPECTION &amp; TESTING CONSULTING</li>
        <li>TRAINING &amp; EDUCATION</li>
        <li>CERTIFICATION SERVICES</li>
        <li>LEVEL 3 SERVICES</li>
        <li>TORVEX / AUDITING</li>
        <li>INSPECTION SYSTEMS</li>
      </ul>
    </div>
  </section>

</body>
</html>
```